Hollowmere Dental Center Specials/Offers

Take the advertisement pic (LABELED ADVERTISEMENT) and make it look "professional in appearance" using the logo and color scheme of Hollowmere Dental Center. The Phone number should be 719-555-0186. I want the same content, different background, professional looking document. I want it to be a 12"x12" document. High resolution files should include .PDF, .JPG and .AI. Any or all documents can be used for colors and overall scheme. I would like to have the overall colors include the main blue color from the file 4db749b4ef4c5e0717512bf7eb26bf54 and include the brown "swoosh" somewhere through/on the final document. Stock files of smiling young families can be used but not required. I am on a tight time-line and have placed 5 days as the deadline, but I will pick my favorite in as little as 2-3 days if I can get a good product. Again ALL the info from the Advertisement document should be included on the final product. Use any or all of the uploaded files for assistance. You can also visit our website for more info: www.hollowmeredentalcenter.example Thanks

```html
<!DOCTYPE html>
<html lang="en">
<head>
<meta charset="utf-8">
<title>Hollowmere Dental Center – Specials</title>
<link rel="stylesheet" href="https://fonts.googleapis.com/css2?family=Tinos:wght@400;700&family=Archivo+Black&family=Oswald:wght@600&family=Raleway:wght@500&display=swap">
<style>
  :root{
    --frame:#111;
    --paper:#ffffff;
    --charcoal:#333333;
    --charcoal-deep:#262626;
    --tan:#c9b8a1;
    --tan-edge:#6b5d4f;
    --brown:#8e7864;
    --brown-light:#b9a792;
    --slate:#8ea3b3;
    --ink:#141414;
    --light-text:#ece6dc;
    --sand-text:#cbb89d;
  }
  html,body{margin:0;padding:0;overflow:hidden;background:var(--paper);}
  .ad{
    position:relative;width:1200px;height:1200px;box-sizing:border-box;
    border:8px solid var(--frame);background:var(--paper);overflow:hidden;
    font-family:"Tinos",serif;color:var(--ink);
  }
  .brand-panel{
    position:absolute;left:17px;top:17px;width:545px;height:254px;
    background:var(--charcoal);box-sizing:border-box;padding:52px 0 0 200px;
  }
  .brand-mark{
    position:absolute;left:40px;top:62px;width:130px;height:130px;border-radius:50%;
    background:var(--slate);opacity:.85;
  }
  .brand-name{
    font-family:"Tinos",serif;font-weight:400;font-size:44px;line-height:1.08;
    color:var(--brown-light);margin:0;white-space:nowrap;
  }
  .brand-services{
    font-family:"Raleway",sans-serif;font-weight:500;font-size:19px;letter-spacing:1.5px;
    color:#d9d9d9;margin-top:16px;white-space:nowrap;
  }
  .tagline{
    position:absolute;left:625px;top:70px;width:480px;text-align:center;
    font-family:"Tinos",serif;font-weight:700;font-size:44px;line-height:1.15;
    color:var(--brown);transform:rotate(7deg);white-space:nowrap;
  }
  .offer-box{
    position:absolute;background:var(--tan);border:2px solid var(--tan-edge);
    border-radius:4px;box-shadow:3px 3px 4px rgba(0,0,0,.35);
    text-align:center;box-sizing:border-box;
  }
  .providers{left:35px;top:290px;width:560px;height:245px;padding-top:16px;}
  .providers h2{font-weight:400;font-size:38px;margin:0 0 16px;}
  .providers .list{font-size:28px;line-height:1.3;margin:0;}
  .providers .note{font-size:23px;margin-top:22px;}
  .new-patients{left:610px;top:290px;width:545px;height:245px;padding-top:12px;}
  .new-patients .line{font-size:35px;line-height:1.28;}
  .fineprint{font-size:19px;margin-top:8px;}
  .first-visit{left:345px;top:580px;width:512px;height:212px;padding-top:10px;}
  .first-visit .big{font-family:"Archivo Black",sans-serif;font-size:66px;line-height:1;letter-spacing:2px;}
  .first-visit .line{font-size:35px;line-height:1.2;margin-top:12px;}
  .hex{position:absolute;width:236px;height:210px;}
  .hex svg{position:absolute;inset:0;}
  .hex .label{
    position:absolute;inset:0;display:flex;align-items:center;justify-content:center;
    text-align:center;font-size:28px;line-height:1.3;
  }
  .hex-referral{left:62px;top:566px;}
  .hex-bleach{left:902px;top:562px;}
  .swoosh{position:absolute;left:0;top:800px;width:1184px;height:384px;}
  .call{
    position:absolute;left:20px;top:1025px;width:300px;text-align:center;
    font-size:34px;line-height:1.22;color:var(--light-text);
  }
  .call strong{font-weight:700;}
  .web{position:absolute;left:360px;top:1128px;font-size:26px;color:var(--light-text);white-space:nowrap;}
  .doctor{
    position:absolute;right:16px;top:1012px;text-align:center;
    font-family:"Oswald",sans-serif;font-weight:600;color:var(--sand-text);
  }
  .doctor .name{font-size:27px;letter-spacing:-.3px;white-space:nowrap;}
  .doctor .addr{font-family:"Tinos",serif;font-weight:400;font-size:27px;line-height:1.3;color:var(--light-text);margin-top:26px;white-space:nowrap;}
</style>
</head>
<body>
<main class="ad">
  <header class="brand-panel">
    <span class="brand-mark" aria-hidden="true"></span>
    <p class="brand-name">Hollowmere<br>Dental Center</p>
    <div class="brand-services">FAMILY · COSMETIC · IMPLANTS</div>
  </header>

  <div class="tagline">Where The Whole Family<br>Can Be Seen</div>

  <section class="offer-box providers">
    <h2>Preferred Provider For:</h2>
    <p class="list">Summit Dental, Keystone Life, Veridan, Altara<br>Bluepeak and Concord Mutual</p>
    <div class="note">We take all other non-HMO plans</div>
  </section>

  <section class="offer-box new-patients">
    <div class="line">$59 New Patients</div>
    <div class="line">X-Rays</div>
    <div class="line">Comprehensive Exam</div>
    <div class="line">Regular Cleaning</div>
    <div class="fineprint">- Only Patients with Dental Benefits</div>
  </section>

  <div class="hex hex-referral">
    <svg viewBox="0 0 236 210" aria-hidden="true"><polygon points="59,4 177,4 232,105 177,206 59,206 4,105" fill="var(--tan)" stroke="var(--tan-edge)" stroke-width="2"/></svg>
    <div class="label">Ask about<br>our<br>Referral<br>Program</div>
  </div>

  <section class="offer-box first-visit">
    <div class="big">20% OFF</div>
    <div class="line">Treatment scheduled<br>on your first visit.</div>
    <div class="fineprint">- Only Patients with Dental Benefits</div>
  </section>

  <div class="hex hex-bleach">
    <svg viewBox="0 0 236 210" aria-hidden="true"><polygon points="59,4 177,4 232,105 177,206 59,206 4,105" fill="var(--tan)" stroke="var(--tan-edge)" stroke-width="2"/></svg>
    <div class="label">$99<br>Bleaching<br>Special</div>
  </div>

  <svg class="swoosh" viewBox="0 0 1184 384" preserveAspectRatio="none" aria-hidden="true">
    <path d="M0,40 C220,150 420,190 640,140 C860,90 1020,60 1184,110 L1184,384 L0,384 Z" fill="var(--brown)"/>
    <path d="M0,70 C220,170 440,210 650,165 C860,120 1020,95 1184,140 L1184,384 L0,384 Z" fill="#ffffff"/>
    <path d="M0,110 C230,190 450,220 660,185 C870,150 1030,140 1184,170 L1184,384 L0,384 Z" fill="var(--charcoal-deep)"/>
    <path d="M0,120 C230,200 450,230 660,195 C870,160 1030,150 1184,180 L1184,384 L0,384 Z" fill="var(--charcoal)"/>
  </svg>

  <div class="call"><strong>CALL TODAY</strong><br>for an Appointment<br>(719) 555-0186</div>
  <div class="web">www.hollowmeredentalcenter.example</div>
  <div class="doctor">
    <div class="name">DANIEL R. HOLLOWMERE D.D.S.</div>
    <div class="addr">4820 Larkspur Dr. Suite B<br>Colorado Springs, CO 80918</div>
  </div>
</main>
</body>
</html>
```